We want to design total new business card and logo for Kestrel Building Services Ltd

Our company name Kestrel Building Services Ltd. Design new logo and business card , need hi-end luxury style art for architecture and construction industry. The card should simple but stylish. Our business focus on CONNECT tradesman to construction company, help marketing construction company tender oversea projects, managing franchise in construction sector, delivery amazing services to our client, so Logo should show the CONNECTION IDEA, CONNECTING PEOPLE, LUXURY. Visit our website for more information: kestrelhub.co.nz

Low design quality

Target Market(s)

Directors or managers

Industry/Entity Type

Construction Company

Contact Information for Business Card

Name, Title, Mobile, Email, Website

Font styles to use
Serif

Colors

Designer to choose colors to be used in the design.

Requirements
Must have
• Simple and luxury, connection icon
Nice to have
• Special materials, plastic card, look through,...
• Look new ideas.

```html
<!DOCTYPE html>
<html lang="en">
<head>
<meta charset="utf-8">
<title>Kestrel Building Services Ltd — Business Card</title>
<link href="https://fonts.googleapis.com/css2?family=Montserrat:wght@400;500&display=swap" rel="stylesheet">
<style>
  :root {
    --backdrop: #1e1e1e;
    --card: #262626;
    --card-edge: #2e2e2e;
    --silver: #b9b9b9;
    --brand-blue: #1a5fb4;
    --ink-white: #f2f2f2;
  }
  * { margin: 0; padding: 0; box-sizing: border-box; }
  html, body { width: 1200px; height: 900px; overflow: hidden; }
  body {
    background: var(--backdrop);
    font-family: "Montserrat", sans-serif;
    position: relative;
  }
  .card {
    position: absolute;
    left: 250px;
    width: 700px;
    height: 400px;
    background: linear-gradient(135deg, var(--card) 0%, var(--card-edge) 100%);
    border-radius: 2px;
  }
  .card--front { top: 40px; }
  .card--back { top: 465px; }

  .front-name {
    position: absolute;
    left: 0; right: 0; top: 170px;
    text-align: center;
    color: var(--silver);
    font-weight: 500;
    font-size: 30px;
    letter-spacing: 1px;
    line-height: 1.3;
  }

  .back-name {
    position: absolute;
    left: 50px; top: 150px;
    width: 250px;
    color: var(--brand-blue);
    font-weight: 500;
    font-size: 26px;
    line-height: 1.3;
    text-align: center;
  }
  .divider {
    position: absolute;
    left: 345px; top: 90px;
    width: 2px; height: 220px;
    background: var(--brand-blue);
  }
  .contact {
    position: absolute;
    left: 380px; top: 95px;
    color: var(--ink-white);
  }
  .contact__name {
    color: var(--brand-blue);
    font-weight: 500;
    font-size: 26px;
    text-transform: uppercase;
    line-height: 1.1;
  }
  .contact__title { font-size: 17px; margin-bottom: 16px; }
  .contact__address { font-size: 17px; line-height: 1.35; margin-bottom: 14px; }
  .contact__list { list-style: none; font-size: 17px; line-height: 1.6; }
  .contact__list li { display: flex; align-items: center; gap: 10px; }
  .contact__list svg { width: 14px; height: 14px; flex: none; }
</style>
</head>
<body>
  <section class="card card--front">
    <p class="front-name">Kestrel Building<br>Services Ltd</p>
  </section>

  <section class="card card--back">
    <p class="back-name">Kestrel Building Services Ltd</p>
    <div class="divider"></div>
    <div class="contact">
      <p class="contact__name">Daniel Hartley</p>
      <p class="contact__title">Director</p>
      <p class="contact__address">52 Quarry Lane<br>Millbrook, NC 28000</p>
      <ul class="contact__list">
        <li>
          <svg viewBox="0 0 16 16" fill="none" stroke="#1a5fb4" stroke-width="1.6"><path d="M4 1.5l2.5 3-1.5 1.5c1 2 2.5 3.5 4.5 4.5l1.5-1.5 3 2.5-1.5 2.5C7 14 2 9 1.5 3z"/></svg>
          +330 5550-1234
        </li>
        <li>
          <svg viewBox="0 0 16 16" fill="#1a5fb4"><rect x="4" y="1" width="8" height="4"/><rect x="1" y="6" width="14" height="6" rx="1"/><rect x="4" y="10" width="8" height="5" fill="#262626" stroke="#1a5fb4"/></svg>
          +330 5550-1278
        </li>
        <li>
          <svg viewBox="0 0 16 16" fill="none" stroke="#1a5fb4" stroke-width="1.4"><rect x="1.5" y="3.5" width="13" height="9"/><path d="M1.5 3.5l6.5 5 6.5-5"/></svg>
          info@kestrelhub.co.nz
        </li>
        <li>
          <svg viewBox="0 0 16 16" fill="none" stroke="#1a5fb4" stroke-width="1.3"><circle cx="8" cy="8" r="6.5"/><ellipse cx="8" cy="8" rx="3" ry="6.5"/><path d="M1.5 8h13"/></svg>
          www.kestrelhub.co.nz
        </li>
      </ul>
    </div>
  </section>
</body>
</html>
```